Temporary tattoo(s) envelope.

We need an envelope design for new company based in Europe called inkpetals.com. We would like to see our product presented/wrapped up in enticing, modern/minimal and latest tattoo trend/fashion related way. Homepage related colours welcome although not a must (relate to the website, 'inkpetals.com' ).
Rag paper envelope size 10cm x 5cm.

Target Market(s)

Target customers kids/teenagers also mostly females up to 35 years old.

Industry/Entity Type

Tattoo

Colors

Designer to choose colors to be used in the design.

```html
<!DOCTYPE html>
<html lang="en">
<head>
<meta charset="utf-8">
<title>inkpetals.com envelope</title>
<link href="https://fonts.googleapis.com/css2?family=Yanone+Kaffeesatz:wght@300;400&display=swap" rel="stylesheet">
<style>
  :root {
    --backdrop: #dedede;
    --paper-top: #f8f6f7;
    --paper-bottom: #cdcbcc;
    --ink: #111111;
    --paper-text: #ffffff;
    --window: #f1f1f1;
    --window-edge: #d4d2d3;
    --fold-line: #9c9a9b;
  }
  html, body {
    margin: 0;
    padding: 0;
    width: 1200px;
    height: 750px;
    overflow: hidden;
    background: var(--backdrop);
  }
  .canvas {
    position: relative;
    width: 1200px;
    height: 750px;
  }
  .envelope {
    position: absolute;
    top: 250px;
    width: 500px;
    height: 250px;
    display: block;
    filter: drop-shadow(0 6px 10px rgba(0,0,0,0.12));
  }
  .envelope--back { left: 60px; }
  .envelope--front { left: 640px; }
  .brand-text {
    font-family: 'Yanone Kaffeesatz', sans-serif;
    font-weight: 400;
  }
  .tab-name {
    fill: var(--paper-text);
    font-size: 17px;
    letter-spacing: 0.5px;
  }
  .seal-name {
    fill: var(--ink);
    font-size: 17px;
    letter-spacing: 0.5px;
  }
  .web-address {
    fill: var(--ink);
    font-family: 'Yanone Kaffeesatz', sans-serif;
    font-weight: 300;
    font-size: 14px;
    letter-spacing: 0.8px;
  }
</style>
</head>
<body>
<main class="canvas">

  <!-- Envelope back: sealed flap -->
  <svg class="envelope envelope--back" viewBox="0 0 500 250" aria-label="Envelope back with black flap band">
    <defs>
      <linearGradient id="paperBack" x1="0" y1="0" x2="0" y2="1">
        <stop offset="0" stop-color="var(--paper-top)"/>
        <stop offset="1" stop-color="var(--paper-bottom)"/>
      </linearGradient>
    </defs>
    <rect class="paper" x="0" y="0" width="500" height="250" fill="url(#paperBack)" stroke="var(--fold-line)" stroke-width="0.6"/>
    <polygon class="flap-band" points="0,0 500,0 470,62 18,62" fill="var(--ink)"/>
    <g class="seal">
      <circle cx="228" cy="62" r="22" fill="var(--ink)" stroke="var(--paper-text)" stroke-width="2"/>
      <text class="brand-text seal-name" x="258" y="96">inkpetals.com</text>
    </g>
  </svg>

  <!-- Envelope front: address side with window -->
  <svg class="envelope envelope--front" viewBox="0 0 500 250" aria-label="Envelope front with address window">
    <defs>
      <linearGradient id="paperFront" x1="0" y1="0" x2="0" y2="1">
        <stop offset="0" stop-color="#d6d4d5"/>
        <stop offset="0.6" stop-color="#efedee"/>
        <stop offset="1" stop-color="var(--paper-top)"/>
      </linearGradient>
    </defs>
    <rect class="paper" x="0" y="0" width="500" height="250" fill="url(#paperFront)"/>
    <rect class="top-rule" x="0" y="0" width="500" height="4" fill="var(--ink)"/>
    <polygon class="name-tab" points="70,0 190,0 190,28 130,46 70,28" fill="var(--ink)"/>
    <text class="brand-text tab-name" x="130" y="26" text-anchor="middle">inkpetals.com</text>
    <rect class="address-window" x="60" y="140" width="200" height="72" rx="8" fill="var(--window)" stroke="var(--window-edge)" stroke-width="1.5"/>
    <text class="web-address" x="488" y="236" text-anchor="end">www.inkpetals.com</text>
    <rect class="bottom-rule" x="0" y="244" width="500" height="6" fill="var(--ink)"/>
  </svg>

</main>
</body>
</html>
```